Verostel business card

Business card for sustainable investment company called "Verostel". Verostel is an exchange platform selling carbon credits between buyers and sellers. Carbon Credits are an environmental commodity for reducing global carbon emissions.

the card should obviously have our logo and the theme should be sustainability/environment mixed with a trading platform.

Contact Information for Business Card

Logo, Name, Title, Phone, Email

Colors
0054AA
0677BA
7BADD7
CADEEF
E8F1F8
0094D4
00A9DD
6FCCEA
C7EBF8
E9F6FB
00AB8E
00BBA5
67D7C9
C6EFE9
E9F9F6
59FF00
82FF00
B8FF75
E3FFCB
F4FFEA

```html
<!DOCTYPE html>
<html lang="en">
<head>
<meta charset="utf-8">
<title>Verostel business card</title>
<link rel="stylesheet" href="https://fonts.googleapis.com/css2?family=Montserrat:wght@400;500;700&display=swap">
<style>
  :root {
    --backdrop: #2399ad;
    --kraft: #e7e0d3;
    --kraft-shade: #ddd5c6;
    --ink: #1b2a3d;
    --ink-soft: #3a4350;
    --teal: #00bba5;
    --aqua: #00a9dd;
    --blue: #0677ba;
    --deep-blue: #0054aa;
  }
  * { margin: 0; padding: 0; box-sizing: border-box; }
  html, body { width: 1200px; height: 1200px; overflow: hidden; }
  body {
    background: var(--backdrop);
    font-family: "Montserrat", sans-serif;
    color: var(--ink);
    position: relative;
  }
  .card {
    position: absolute;
    left: 220px;
    width: 760px;
    height: 434px;
    border-radius: 30px;
    background: radial-gradient(circle at 30% 30%, var(--kraft) 0%, var(--kraft-shade) 100%);
    box-shadow: 0 14px 30px rgba(0, 40, 50, 0.35);
    overflow: hidden;
  }
  .card--front { top: 136px; }
  .card--back { top: 630px; }

  .brand { display: flex; align-items: center; gap: 16px; }
  .brand__square {
    width: 44px; height: 44px; border-radius: 6px;
    background: linear-gradient(135deg, var(--teal), var(--blue));
  }
  .brand__name {
    font-weight: 700;
    letter-spacing: 1px;
    text-transform: uppercase;
    color: var(--ink);
  }

  .card--front .brand { position: absolute; left: 190px; top: 110px; }
  .card--front .brand__name { font-size: 52px; }

  .person { position: absolute; left: 84px; top: 300px; padding-left: 18px; }
  .person::before {
    content: ""; position: absolute; left: 0; top: 4px; width: 5px; height: 62px;
    background: linear-gradient(180deg, var(--aqua), var(--blue));
  }
  .person__name { font-size: 30px; font-weight: 500; color: var(--aqua); letter-spacing: 0.5px; }
  .person__title { font-size: 18px; font-weight: 400; color: var(--ink-soft); letter-spacing: 1px; margin-top: 2px; }

  .divider { position: absolute; left: 420px; top: 240px; width: 1px; height: 120px; background: var(--ink-soft); }

  .contacts { position: absolute; left: 460px; top: 246px; list-style: none; }
  .contacts li { display: flex; align-items: center; gap: 10px; font-size: 19px; color: var(--ink-soft); height: 36px; }
  .contacts svg { width: 20px; height: 20px; flex: none; }

  .card--back .brand { position: absolute; left: 70px; top: 250px; }
  .card--back .brand__name { font-size: 60px; }
  .card--back .brand__square { width: 52px; height: 52px; }
  .accent-field {
    position: absolute; right: 0; top: 0; width: 280px; height: 100%;
    background: linear-gradient(160deg, var(--blue) 0%, var(--aqua) 55%, var(--teal) 100%);
    opacity: 0.9;
  }
</style>
</head>
<body>
  <section class="card card--front" aria-label="Business card front">
    <div class="brand">
      <span class="brand__square"></span>
      <span class="brand__name">Verostel</span>
    </div>
    <div class="person">
      <p class="person__name">FULL NAME</p>
      <p class="person__title">POSITION</p>
    </div>
    <span class="divider"></span>
    <ul class="contacts">
      <li>
        <svg viewBox="0 0 24 24" aria-hidden="true"><path fill="#00a9dd" d="M6.6 10.8a15 15 0 0 0 6.6 6.6l2.2-2.2a1 1 0 0 1 1-.25 11.4 11.4 0 0 0 3.6.57 1 1 0 0 1 1 1V20a1 1 0 0 1-1 1A17 17 0 0 1 3 4a1 1 0 0 1 1-1h3.5a1 1 0 0 1 1 1 11.4 11.4 0 0 0 .57 3.6 1 1 0 0 1-.25 1z"/></svg>
        (000) 000 0000
      </li>
      <li>
        <svg viewBox="0 0 24 24" aria-hidden="true"><rect x="2" y="5" width="20" height="14" rx="1" fill="#0677ba"/><path d="M2 6l10 7 10-7" fill="none" stroke="#e7e0d3" stroke-width="1.5"/></svg>
        hello@verostel.com
      </li>
      <li>
        <svg viewBox="0 0 24 24" aria-hidden="true" fill="none" stroke="#0677ba" stroke-width="1.6"><circle cx="12" cy="12" r="9.5"/><ellipse cx="12" cy="12" rx="4.5" ry="9.5"/><path d="M2.5 12h19M4 7h16M4 17h16"/></svg>
        www.verostel.com
      </li>
    </ul>
  </section>

  <section class="card card--back" aria-label="Business card back">
    <div class="accent-field" role="img" aria-label="Brand gradient decoration"></div>
    <div class="brand">
      <span class="brand__square"></span>
      <span class="brand__name">Verostel</span>
    </div>
  </section>
</body>
</html>
```